Wyoming Local Silver Creek Nectar - sticker for retail jars

I am looking for a simple, western mountain style label for my honey jars.
I am open to any color. Natural colors seem more appealing to me for this.
I also love teal and red.
I live in Wyoming. Silver creek nectar.
I have attached a couple of things that may like to either incorporate or keep a similar style.
Although, with my honey jars, I do prefer a very simple, wholesome, old-timey feel to the label. Possibly printing on a craft paper color of sticker.

Target Market(s)

local store, farmers market

Industry/Entity Type

Agriculture

Requirements
Must have
• I think I would like the main title to by Silver Creek Nectar ... then include my city and state (Alder Falls, Eastmoor) somewhere on the sticker
Nice to have
• I recently had a logo design done... it would be nice to have this incorporated somewhere subtly on the sticker.

```html
<!DOCTYPE html>
<html lang="en">
<head>
<meta charset="utf-8">
<title>Silver Creek Nectar – Jar Sticker</title>
<link rel="stylesheet" href="https://fonts.googleapis.com/css2?family=EB+Garamond:wght@400;700&display=swap">
<style>
  :root {
    --bark: #3c2415;
    --honey: #fbae17;
    --shade: #b3b3b3;
    --paper: #ffffff;
    --comb: #fdeccb;
  }
  html, body {
    margin: 0;
    padding: 0;
    width: 1200px;
    height: 1086px;
    overflow: hidden;
    background: var(--paper);
  }
  .sticker {
    display: block;
    width: 1200px;
    height: 1086px;
  }
  .scallop-shadow { fill: var(--shade); stroke: var(--shade); }
  .scallop-outer  { fill: var(--bark);  stroke: var(--bark); }
  .scallop-inner  { fill: var(--honey); stroke: var(--honey); }
  .face-ring { fill: url(#faceGlow); stroke: var(--bark); stroke-width: 5; }
  .mountain-art { fill: url(#peakTone); }
  .label-text {
    font-family: "EB Garamond", "Garamond", serif;
    font-size: 66px;
    fill: var(--bark);
    text-anchor: middle;
  }
  .label-text--title { font-weight: 700; }
</style>
</head>
<body>
<svg class="sticker" viewBox="0 0 1200 1086" xmlns="http://www.w3.org/2000/svg">
  <defs>
    <radialGradient id="faceGlow" cx="0.5" cy="0.5" r="0.5">
      <stop offset="0" stop-color="#ffffff"/>
      <stop offset="1" stop-color="#fffaf0"/>
    </radialGradient>
    <linearGradient id="peakTone" x1="0" y1="0" x2="0" y2="1">
      <stop offset="0" stop-color="#5a3a24"/>
      <stop offset="1" stop-color="#3c2415"/>
    </linearGradient>
  </defs>

  <g class="badge-edge">
    <g transform="translate(8 12)">
      <circle class="scallop-shadow" cx="600" cy="520" r="362" stroke-width="60"
              stroke-dasharray="0 63.18" stroke-linecap="round"/>
      <circle class="scallop-shadow" cx="600" cy="520" r="362" stroke="none"/>
    </g>
    <circle class="scallop-outer" cx="600" cy="520" r="362" stroke-width="60"
            stroke-dasharray="0 63.18" stroke-linecap="round"/>
    <circle class="scallop-outer" cx="600" cy="520" r="362" stroke="none"/>
    <circle class="scallop-inner" cx="600" cy="520" r="340" stroke-width="50"
            stroke-dasharray="0 59.34" stroke-linecap="round"/>
    <circle class="scallop-inner" cx="600" cy="520" r="340" stroke="none"/>
  </g>

  <circle class="face-ring" cx="600" cy="526" r="327"/>

  <rect class="mountain-art" x="430" y="268" width="340" height="176" rx="10"
        role="img" aria-label="Illustration of rugged mountain peaks with snow"/>

  <g class="label-copy">
    <text class="label-text" x="600" y="503">Silver Creek</text>
    <text class="label-text label-text--title" x="600" y="565">Nectar.</text>
    <text class="label-text" x="600" y="628">Locally harvested,</text>
    <text class="label-text" x="600" y="690">Alder Falls, Eastmoor.</text>
    <text class="label-text" x="600" y="752">K7 Ranch Co.</text>
  </g>
</svg>
</body>
</html>
```